KVRo Business Cards

We need a business card design. We are a Technology (Audio Visual) design, sales and installation company. Looking for a double sided design, clean

Contact Information for Business Card

Clean, modern look, 2 sided

Font styles to use
Sans Serif

```html
<!DOCTYPE html>
<html lang="en">
<head>
<meta charset="utf-8">
<title>KVRo Business Card</title>
<link rel="stylesheet" href="https://fonts.googleapis.com/css2?family=Montserrat:wght@400;500;600;700;800&display=swap">
<style>
  :root {
    --page-bg: #f1f1f1;
    --navy: #1e3040;
    --orange: #f7961e;
    --white: #ffffff;
    --label: #555b61;
    --muted: #e4e7ea;
  }
  * { box-sizing: border-box; margin: 0; padding: 0; }
  html, body { width: 717px; height: 1200px; overflow: hidden; }
  body {
    background: var(--page-bg);
    font-family: "Montserrat", Arial, sans-serif;
    position: relative;
  }
  .sheet-title {
    position: absolute; left: 58px; top: 30px;
    font-size: 17px; font-weight: 500; color: var(--label);
  }
  .card {
    position: absolute; left: 108px; width: 502px; height: 287px;
    overflow: hidden; box-shadow: 0 1px 3px rgba(0,0,0,.12);
  }
  .card-front { top: 96px; background: var(--white); }
  .card-back { top: 404px; background: var(--orange); }

  .brand-name {
    position: absolute; left: 32px; top: 66px;
    font-size: 46px; font-weight: 800; color: var(--navy); letter-spacing: -1px;
  }
  .name-band {
    position: absolute; left: 0; top: 172px; width: 238px; height: 44px;
    background: var(--orange); text-align: right; padding: 6px 16px 0 0;
    color: var(--navy);
  }
  .owner-name { font-size: 14px; font-weight: 700; line-height: 1.2; }
  .designation { font-size: 10px; font-weight: 500; }

  .contact-panel {
    position: absolute; left: 238px; top: 0; width: 264px; height: 100%;
    background: var(--navy); padding: 30px 0 0 18px;
  }
  .contact-row {
    display: flex; align-items: center; gap: 14px; height: 50px;
    color: var(--white); font-size: 12px; font-weight: 500; line-height: 1.3;
  }
  .contact-icon { width: 24px; height: 24px; flex: none; }

  .back-brand {
    position: absolute; left: 0; right: 0; top: 92px; text-align: center;
    font-size: 104px; font-weight: 800; color: var(--white); letter-spacing: -3px;
    line-height: 1;
  }
  .back-web {
    position: absolute; left: 0; right: 0; bottom: 30px; text-align: center;
    font-size: 14px; font-weight: 600; color: var(--navy);
  }
</style>
</head>
<body>
  <h1 class="sheet-title">Business Card: Dimensions 3.5" x 2.0"</h1>

  <section class="card card-front" aria-label="Card front">
    <div class="brand-name">KVRo</div>
    <div class="name-band">
      <div class="owner-name">Owner's Name</div>
      <div class="designation">Designation</div>
    </div>
    <div class="contact-panel">
      <div class="contact-row">
        <svg class="contact-icon" viewBox="0 0 24 24" fill="none" stroke="#fff" stroke-width="1.4">
          <circle cx="12" cy="12" r="11"/><rect x="8.5" y="6" width="7" height="12" rx="1.2"/><line x1="11" y1="15.8" x2="13" y2="15.8"/>
        </svg>
        <span>555-201-4480 - dummy no.</span>
      </div>
      <div class="contact-row">
        <svg class="contact-icon" viewBox="0 0 24 24" fill="none" stroke="#fff" stroke-width="1.4">
          <circle cx="12" cy="12" r="11"/><rect x="6.5" y="8" width="11" height="8" rx="1"/><polyline points="6.5,8.5 12,12.5 17.5,8.5"/>
        </svg>
        <span>info@kvro.com</span>
      </div>
      <div class="contact-row">
        <svg class="contact-icon" viewBox="0 0 24 24" fill="none" stroke="#fff" stroke-width="1.4">
          <circle cx="12" cy="12" r="11"/><path d="M12 18s-4-4.3-4-7.2a4 4 0 0 1 8 0C16 13.7 12 18 12 18z"/><circle cx="12" cy="10.8" r="1.4"/>
        </svg>
        <span>Company address and or<br>branch address</span>
      </div>
      <div class="contact-row">
        <svg class="contact-icon" viewBox="0 0 24 24" fill="none" stroke="#fff" stroke-width="1.4">
          <circle cx="12" cy="12" r="11"/><circle cx="12" cy="12" r="5.5"/><ellipse cx="12" cy="12" rx="2.4" ry="5.5"/><line x1="6.5" y1="12" x2="17.5" y2="12"/>
        </svg>
        <span>www.kvro.com</span>
      </div>
    </div>
  </section>

  <section class="card card-back" aria-label="Card back">
    <div class="back-brand">KVRo</div>
    <div class="back-web">www.kvro.com</div>
  </section>
</body>
</html>
```